Wordpress website update with basic ecomm features

We need an update to our existing website
www.quillharbour.com.au that can be easily updated, enhances our logo and can take payments online and a basic text logo suite for 3 products. Website would reflect confidence and give clients confidence in the outcomes we will provide for them. must be easy to use, crisp, fresh, clean and dynamic.

Target Market(s)

entrepreneurs, professionals, small business owners, corporate organisations, universities

Industry/Entity Type

Online

Coding

Coded - Design and coding required

Number of Pages Required

5+ page

Font styles to use
Sans Serif

Requirements
Must have
• be easy to navigate, look professional, please see brief doc
Nice to have
• please see briefing doc
Should not have
• please see briefing doc

```html
<!DOCTYPE html>
<html lang="en">
<head>
<meta charset="utf-8">
<title>Quill Harbour</title>
<link href="https://fonts.googleapis.com/css2?family=Open+Sans:wght@400;600;700;800&family=Roboto:wght@400;500&display=swap" rel="stylesheet">
<style>
:root{
  --ink:#111;
  --text:#333;
  --muted:#888;
  --rule:#e2e2e2;
  --panel:#f5f5f5;
  --bar:#e4e4e4;
  --badge:#4a4a4a;
  --white:#fff;
}
*{box-sizing:border-box;margin:0;padding:0}
html,body{width:1200px;height:3035px;overflow:hidden;background:var(--white)}
body{font-family:'Open Sans',sans-serif;color:var(--text);position:relative}
/* header */
.site-header{position:absolute;left:0;top:0;width:1200px;height:174px}
.brand{position:absolute;left:131px;top:32px;width:140px;text-align:center}
.brand-square{width:94px;height:94px;background:var(--ink);border-radius:6px;margin:0 auto}
.brand-name{display:block;margin-top:10px;font-size:10.5px;font-weight:600;color:var(--ink);letter-spacing:1.6px;text-transform:uppercase;white-space:nowrap}
.main-nav{position:absolute;right:134px;top:72px;display:flex;gap:28px;font-size:11.5px;text-transform:uppercase;color:#444}
.main-nav .active{color:var(--ink);border-bottom:1px solid var(--ink);padding-bottom:2px}
/* hero */
.hero{position:absolute;left:0;top:174px;width:1200px;height:440px;
  background:
    radial-gradient(ellipse 170px 190px at 840px 180px,rgba(150,110,85,.75),rgba(150,110,85,0) 100%),
    radial-gradient(ellipse 260px 200px at 860px 420px,rgba(125,140,150,.8),rgba(125,140,150,0) 100%),
    radial-gradient(ellipse 360px 260px at 380px 140px,rgba(255,255,255,.9),rgba(255,255,255,0) 100%),
    radial-gradient(ellipse 200px 260px at 1120px 200px,rgba(120,90,60,.55),rgba(120,90,60,0) 100%),
    linear-gradient(90deg,#7a6556 0%,#c9bcac 18%,#efebe5 40%,#ddd4c8 58%,#b9a894 78%,#8f7a62 100%)}
.hero-title{position:absolute;left:132px;top:176px}
.hero-title span{display:inline-block;background:rgba(255,255,255,.6);color:var(--ink);font-size:22px;font-weight:600;padding:4px 10px;margin-bottom:8px;text-transform:uppercase}
.dots{display:flex;gap:8px;justify-content:center}
.dots i{display:block;width:8px;height:8px;border-radius:50%;border:1px solid var(--white)}
.dots i.on{background:var(--white)}
.hero .dots{position:absolute;left:0;right:0;top:408px}
.dots.dark i{border-color:#bbb;background:#ccc}
.dots.dark i.on{background:var(--ink);border-color:var(--ink)}
.section-title{font-size:27px;font-weight:700;color:var(--ink);text-align:center;text-transform:uppercase}
/* welcome */
.welcome{position:absolute;left:0;top:614px;width:1200px;height:514px}
.welcome .section-title{position:absolute;top:72px;width:100%}
.intro{position:absolute;left:130px;top:124px;width:940px;font-size:11.5px;line-height:21px;color:var(--muted);text-align:center}
.feature{position:absolute;top:250px;width:260px;text-align:center}
.feature-icon{width:96px;height:96px;margin:0 auto;border:2px solid #bbb;border-radius:6px;display:flex;align-items:center;justify-content:center}
.feature-icon div{width:80px;height:80px;background:#2b2b2b;border-radius:3px;display:flex;align-items:center;justify-content:center}
.feature h3{font-size:18px;font-weight:700;color:var(--ink);margin-top:18px;text-transform:uppercase}
.feature p{font-size:10.5px;line-height:17px;color:var(--muted);margin-top:8px}
/* projects */
.projects{position:absolute;left:0;top:1128px;width:1200px;height:510px;background:var(--panel)}
.projects .section-title{position:absolute;top:60px;width:100%}
.card{position:absolute;top:117px;width:217px;height:288px;background:var(--white)}
.card .photo{height:143px}
.card h4{font-size:12px;font-weight:400;color:var(--ink);line-height:17px;margin:18px 18px 0}
.card p{font-size:10px;color:var(--muted);line-height:15px;margin:10px 18px 0}
.projects .dots{position:absolute;left:0;right:0;top:436px}
.photo-sprout{background:radial-gradient(ellipse 40px 50px at 110px 70px,#7f9a4a,rgba(127,154,74,0) 100%),radial-gradient(ellipse 120px 40px at 110px 120px,#d9b394,rgba(217,179,148,0) 100%),linear-gradient(180deg,#eef1e6 0%,#dfe4cf 55%,#cdb9a2 100%)}
.photo-bulbs{background:radial-gradient(ellipse 50px 40px at 110px 80px,#3a3a3a,rgba(58,58,58,0) 100%),radial-gradient(ellipse 90px 30px at 110px 40px,rgba(80,80,80,.45),rgba(80,80,80,0) 100%),linear-gradient(180deg,#f0f0f0,#d4d4d4)}
.photo-laptop{background:radial-gradient(ellipse 60px 40px at 90px 95px,#3f6b9a,rgba(63,107,154,0) 100%),radial-gradient(ellipse 50px 30px at 170px 80px,rgba(180,80,80,.5),rgba(180,80,80,0) 100%),linear-gradient(180deg,#4a4e54,#1c1e21)}
.photo-business{background:radial-gradient(ellipse 45px 80px at 110px 110px,#4f78b8,rgba(79,120,184,0) 100%),linear-gradient(180deg,#f4f6f9,#d6dfeb)}
/* partners */
.partners{position:absolute;left:0;top:1638px;width:1200px;height:205px}
.partners h2{position:absolute;top:64px;width:100%;text-align:center;font-size:17px;font-weight:600;color:var(--ink)}
.partner-row{position:absolute;left:132px;top:114px;width:936px;height:24px;display:flex;justify-content:space-between;align-items:center}
.partner-badge{height:12px;background:var(--badge);border-radius:6px;opacity:.8}
.partners hr{position:absolute;left:132px;top:200px;width:936px;border:0;border-top:1px solid var(--rule)}
/* posts */
.feed{position:absolute;top:1910px;width:456px}
.feed-head{display:flex;justify-content:space-between;align-items:center}
.feed-head h2{font-size:27px;font-weight:700;color:var(--ink);text-transform:uppercase}
.arrows{display:flex;gap:4px}
.arrows span{width:25px;height:25px;border:1px solid #555;display:flex;align-items:center;justify-content:center}
.underline{width:124px;height:3px;background:var(--ink);margin-top:12px}
.post{display:flex;gap:16px;margin-top:52px}
.post .photo{width:186px;height:145px;flex:none}
.post h4{font-family:'Roboto',sans-serif;font-size:14px;font-weight:500;color:var(--ink)}
.post time{display:block;font-family:'Roboto',sans-serif;font-size:10px;font-style:italic;color:#444;margin-top:8px}
.post p{font-family:'Roboto',sans-serif;font-size:11px;line-height:20px;color:#444;margin-top:8px}
.photo-team{background:radial-gradient(ellipse 50px 60px at 40px 60px,#5d7fb0,rgba(93,127,176,0) 100%),radial-gradient(ellipse 60px 50px at 140px 55px,#6a8dbf,rgba(106,141,191,0) 100%),radial-gradient(ellipse 100px 30px at 100px 120px,#e6ddd0,rgba(230,221,208,0) 100%),linear-gradient(180deg,#dde3ea,#b7c4d4)}
.photo-talk{background:radial-gradient(ellipse 45px 60px at 55px 70px,#6f7a86,rgba(111,122,134,0) 100%),radial-gradient(ellipse 45px 60px at 140px 75px,#5a6878,rgba(90,104,120,0) 100%),radial-gradient(ellipse 60px 40px at 100px 40px,#f1ece4,rgba(241,236,228,0) 100%),linear-gradient(180deg,#c9c2b8,#8a8f96)}
/* quote */
.quote{position:absolute;left:0;top:2238px;width:1200px;height:240px;
  background:
    radial-gradient(ellipse 220px 200px at 420px 170px,rgba(205,170,130,.85),rgba(205,170,130,0) 100%),
    radial-gradient(ellipse 200px 160px at 800px 90px,rgba(220,190,165,.7),rgba(220,190,165,0) 100%),
    linear-gradient(90deg,#6a5a4c 0%,#9a8470 30%,#8c8580 55%,#6f7f92 75%,#4b6683 100%)}
.quote::before{content:"";position:absolute;inset:0;background:rgba(30,30,30,.25)}
.quote blockquote{position:absolute;top:56px;width:100%;text-align:center;color:var(--white);font-size:23px;font-weight:700;line-height:32px}
.quote cite{position:absolute;top:130px;width:100%;text-align:center;color:var(--white);font-size:10px;font-style:normal}
.quote .dots{position:absolute;left:0;right:0;top:156px}
/* footer */
.subscribe{position:absolute;left:132px;top:2560px;width:433px;height:367px;background:#0a0a0a;color:var(--white)}
.sub-brand{position:absolute;left:30px;top:28px;width:80px;text-align:center}
.sub-brand .mark{width:58px;height:58px;border:2px solid var(--white);border-radius:4px;margin:0 auto}
.sub-brand span{display:block;margin-top:6px;font-size:7px;letter-spacing:1px;text-transform:uppercase;white-space:nowrap}
.subscribe h3{position:absolute;left:140px;top:26px;font-size:21px;font-weight:600;text-transform:uppercase}
.subscribe .lede{position:absolute;left:140px;top:60px;width:270px;font-size:12px;line-height:19px}
.field{position:absolute;left:44px;width:347px;border-bottom:1px solid var(--white);font-size:13px;padding-bottom:9px}
.signup{position:absolute;left:38px;top:300px;width:114px;height:40px;background:var(--white);color:var(--ink);font-size:13px;font-weight:700;display:flex;align-items:center;justify-content:center;border-radius:3px}
.privacy{position:absolute;left:176px;top:312px;font-size:12px}
.contact{position:absolute;left:604px;top:2563px;width:470px}
.contact h3{font-size:28px;font-weight:400;color:var(--ink)}
.contact .ask{font-size:19px;color:var(--ink);margin-top:20px}
.contact ul{list-style:none;font-size:12px;line-height:23px;color:#333;margin-top:14px}
.contact-line{display:flex;align-items:center;gap:16px;font-size:16px;color:var(--ink)}
.contact-line .ring{width:40px;height:40px;border:2px solid var(--ink);border-radius:50%;display:flex;align-items:center;justify-content:center}
.bottom-bar{position:absolute;left:0;top:2975px;width:1200px;height:60px;background:var(--bar)}
.bottom-bar p{position:absolute;left:132px;top:24px;font-size:10.5px;color:#222}
.social{position:absolute;right:132px;top:12px;display:flex;gap:10px}
.social span{width:36px;height:36px;border:2px solid #222;border-radius:50%;display:flex;align-items:center;justify-content:center}
</style>
</head>
<body>
<header class="site-header">
  <div class="brand"><div class="brand-square"></div><span class="brand-name">Quill Harbour</span></div>
  <nav class="main-nav">
    <span class="active">Why Quill Harbour</span><span>About our offerings</span><span>FAQ</span><span>Testimonials</span><span>Events</span><span>Payments</span>
  </nav>
</header>

<section class="hero" role="img" aria-label="Smiling entrepreneur in a bright studio with large windows and potted plants">
  <div class="hero-title"><span>Australian Business</span><br><span>Entrepreneurship</span></div>
  <div class="dots"><i></i><i class="on"></i><i></i><i></i></div>
</section>

<section class="welcome">
  <h2 class="section-title">Welcome</h2>
  <p class="intro">Fusce posuere urna vel erat posuere gravida. Sed interdum erat dolor, quis vulputate arcu dignissim in. Donec lobortis, sapien eget imperdiet porta, quam ligula blandit tellus, eu fermentum felis nisi ac massa. Sed massa dolor, pharetra nec dignissim eu, hendrerit eget ipsum. Morbi suscipit felis orci, eget condimentum arcu finibus tempor. Nulla facilisi. Proin vel tempus ligula, congue luctus lorem. In convallis, turpis eu tempor facilisis, lacus libero placerat tortor, ac auctor mauris arcu sed urna. Cras sagittis mattis lacinia. Sed tristique sapien nec pellentesque sagittis. Vivamus quis quam at dolor luctus aliquam vel at leo.</p>
  <div class="feature" style="left:135px">
    <div class="feature-icon"><div><svg width="40" height="34" viewBox="0 0 40 34"><rect x="13" y="2" width="14" height="7" fill="none" stroke="#fff" stroke-width="3"/><rect x="2" y="9" width="36" height="23" rx="3" fill="#fff"/><rect x="17" y="17" width="6" height="5" fill="#2b2b2b"/></svg></div></div>
    <h3>Aenean Elementum</h3>
    <p>Morbi suscipit felis orci, eget condimentum arcu finibus tempor. Nulla facilisi. In convallis, turpis eu tempor facilisis, lacus libero placerat tortor.</p>
  </div>
  <div class="feature" style="left:470px">
    <div class="feature-icon"><div><svg width="30" height="42" viewBox="0 0 30 42"><circle cx="15" cy="14" r="12" fill="#fff"/><rect x="9" y="22" width="12" height="9" fill="#fff"/><rect x="9" y="33" width="12" height="3" fill="#fff"/><rect x="11" y="38" width="8" height="3" fill="#fff"/></svg></div></div>
    <h3>Mauris id augue</h3>
    <p>Morbi suscipit felis orci, eget condimentum arcu finibus tempor. Nulla facilisi. In convallis, turpis eu tempor facilisis, lacus libero placerat tortor.</p>
  </div>
  <div class="feature" style="left:805px">
    <div class="feature-icon"><div><svg width="40" height="36" viewBox="0 0 40 36"><path d="M3 2V33H38" fill="none" stroke="#fff" stroke-width="2"/><path d="M8 27L16 15L23 21L33 7" fill="none" stroke="#fff" stroke-width="2"/><circle cx="16" cy="15" r="2.5" fill="#fff"/><circle cx="23" cy="21" r="2.5" fill="#fff"/><circle cx="33" cy="7" r="2.5" fill="#fff"/></svg></div></div>
    <h3>Pellentesque ac orci</h3>
    <p>Morbi suscipit felis orci, eget condimentum arcu finibus tempor. Nulla facilisi. In convallis, turpis eu tempor facilisis, lacus libero placerat tortor.</p>
  </div>
</section>

<section class="projects">
  <h2 class="section-title">Our Projects</h2>
  <article class="card" style="left:132px"><div class="photo photo-sprout" role="img" aria-label="Hand holding soil with a young green sprout"></div><h4>Aenean elementum metus et est pellentesque molestie</h4><p>Aenean interdum sed est sed congue. Cras ac tortor rhoncus felis placerat bibendum. Nulla posuere velit id ornare dapibus. Aenean ultrices.</p></article>
  <article class="card" style="left:372px"><div class="photo photo-bulbs" role="img" aria-label="Sketched light bulbs and currency symbols on a grey wall"></div><h4>Aenean elementum metus et est pellentesque molestie</h4><p>Aenean interdum sed est sed congue. Cras ac tortor rhoncus felis placerat bibendum. Nulla posuere velit id ornare dapibus. Aenean ultrices.</p></article>
  <article class="card" style="left:611px"><div class="photo photo-laptop" role="img" aria-label="Laptop in front of a chalkboard with drawn charts"></div><h4>Aenean elementum metus et est pellentesque molestie</h4><p>Aenean interdum sed est sed congue. Cras ac tortor rhoncus felis placerat bibendum. Nulla posuere velit id ornare dapibus. Aenean ultrices.</p></article>
  <article class="card" style="left:850px"><div class="photo photo-business" role="img" aria-label="Young businessman in a blue shirt with arms crossed"></div><h4>Aenean elementum metus et est pellentesque molestie</h4><p>Aenean interdum sed est sed congue. Cras ac tortor rhoncus felis placerat bibendum. Nulla posuere velit id ornare dapibus. Aenean ultrices.</p></article>
  <div class="dots dark"><i class="on"></i><i></i><i></i><i></i></div>
</section>

<section class="partners">
  <h2>PARTNERS</h2>
  <div class="partner-row">
    <span class="partner-badge" style="width:88px"></span><span class="partner-badge" style="width:94px"></span><span class="partner-badge" style="width:54px;height:20px;border-radius:10px"></span><span class="partner-badge" style="width:110px"></span><span class="partner-badge" style="width:96px"></span><span class="partner-badge" style="width:66px;height:16px"></span><span class="partner-badge" style="width:106px;height:8px"></span>
  </div>
  <hr>
</section>

<section class="feed" style="left:132px">
  <div class="feed-head"><h2>Our Blog Posts</h2><div class="arrows"><span><svg width="8" height="10"><path d="M6 1L2 5L6 9" fill="none" stroke="#111" stroke-width="1.5"/></svg></span><span><svg width="8" height="10"><path d="M2 1L6 5L2 9" fill="none" stroke="#111" stroke-width="1.5"/></svg></span></div></div>
  <div class="underline"></div>
  <div class="post"><div class="photo photo-team" role="img" aria-label="Team gathered around a table reviewing plans"></div>
    <div><h4>Investment &amp; industry partnerships</h4><time>March 20, 2016</time><p>The Quill Harbour builds and develops validation and innovation programs, communities and data to improve the overall success rate of entrepre neurial and early-stage ventures.</p></div></div>
</section>

<section class="feed" style="left:613px">
  <div class="feed-head"><h2>Our Events</h2><div class="arrows"><span><svg width="8" height="10"><path d="M6 1L2 5L6 9" fill="none" stroke="#111" stroke-width="1.5"/></svg></span><span><svg width="8" height="10"><path d="M2 1L6 5L2 9" fill="none" stroke="#111" stroke-width="1.5"/></svg></span></div></div>
  <div class="underline"></div>
  <div class="post"><div class="photo photo-talk" role="img" aria-label="Two colleagues in conversation at a laptop"></div>
    <div><h4>Investment &amp; industry partnerships</h4><time>March 20, 2016</time><p>The Quill Harbour builds and develops validation and innovation programs, communities and data to improve the overall success rate of entrepre neurial and early-stage ventures.</p></div></div>
</section>

<section class="quote" role="img" aria-label="Hand pulling a block from a stacked wooden block tower">
  <blockquote>“ Fusce egestas consectetur nulla, at malesuada purus blandit<br>Nullam varius libero quis odio finibus ”</blockquote>
  <cite>- MARA DELLING</cite>
  <div class="dots"><i class="on"></i><i></i><i></i><i></i></div>
</section>

<section class="subscribe">
  <div class="sub-brand"><div class="mark"></div><span>Quill Harbour</span></div>
  <h3>Subscribe</h3>
  <p class="lede">Sign up with your email address to receive the latest news and updates.</p>
  <div class="field" style="top:144px">First Name</div>
  <div class="field" style="top:192px">Last Name</div>
  <div class="field" style="top:240px">Email Address</div>
  <div class="signup">SIGN UP</div>
  <span class="privacy">We respect your privacy.</span>
</section>

<section class="contact">
  <h3>Quill Harbour</h3>
  <p class="ask">Any Queries? We’d love to hear from you.</p>
  <ul><li>Validation &amp; Business Innovation Programs</li><li>Validation &amp; Innovation Communities</li><li>Entrepreneur &amp; Innovation Data Analytics &amp; Insights</li><li>Commercial Enquiries</li></ul>
  <div class="contact-line" style="margin-top:30px"><span class="ring"><svg width="18" height="14" viewBox="0 0 18 14"><rect width="18" height="14" rx="2" fill="#111"/><path d="M1 2L9 8L17 2" fill="none" stroke="#fff" stroke-width="1.5"/></svg></span>Mail Us At: info@quillharbour.in</div>
  <div class="contact-line" style="margin-top:18px"><span class="ring"><svg width="16" height="16" viewBox="0 0 16 16"><path d="M3 1L6 4L4.5 6.5C5.5 8.5 7.5 10.5 9.5 11.5L12 10L15 13L13 15C7 15 1 9 1 3Z" fill="#111"/></svg></span>Call Us At: +180 010 4477</div>
</section>

<footer class="bottom-bar">
  <p>Copyright © 2016 Quill Harbour. All Right Reserved. Privacy Policy &nbsp;|&nbsp; Harbour secure gateway</p>
  <div class="social" aria-label="Share and follow">
    <span><svg width="16" height="16" viewBox="0 0 16 16"><circle cx="4" cy="8" r="2.2" fill="#222"/><circle cx="12" cy="3.5" r="2.2" fill="#222"/><circle cx="12" cy="12.5" r="2.2" fill="#222"/><path d="M4 8L12 3.5M4 8L12 12.5" stroke="#222" stroke-width="1.3"/></svg></span>
    <span><svg width="16" height="16" viewBox="0 0 16 16"><path d="M2 2H14V11H7L3.5 14V11H2Z" fill="none" stroke="#222" stroke-width="1.6" stroke-linejoin="round"/></svg></span>
    <span><svg width="16" height="14" viewBox="0 0 16 14"><path d="M8 13L2 7A3.3 3.3 0 0 1 8 3A3.3 3.3 0 0 1 14 7Z" fill="#222"/></svg></span>
    <span><svg width="16" height="16" viewBox="0 0 16 16"><path d="M8 1L10 6H15L11 9L12.5 14.5L8 11L3.5 14.5L5 9L1 6H6Z" fill="#222"/></svg></span>
    <span><svg width="16" height="16" viewBox="0 0 16 16"><rect x="1" y="5" width="8" height="6" rx="3" fill="none" stroke="#222" stroke-width="1.6"/><rect x="7" y="5" width="8" height="6" rx="3" fill="none" stroke="#222" stroke-width="1.6"/></svg></span>
  </div>
</footer>
</body>
</html>
```